VelliFilez Website

VelliFiles - Orderly Medical Filez
We need a Web design for a new company called - VelliFilez.
VelliFilez is a Personal Injury and Medical Record Legal Service Outsourcing company. We help Personal Injury Attorneys - with fact based Medical Chronologies and Summaries.

We take Medical Records in disarray and put them in order and summarize them in a chronological order and Update them as needed (if more medical records are added)
Take Releases (for medical records) and work with doctor practices and get the records if needed

Target Market(s)

Personal Injury Attorneys

Industry/Entity Type

Attorney

Number of Pages Required

2 page

Font styles to use
Serif
Sans Serif

Colors

Designer to choose colors to be used in the design.

Requirements
Must have
• Professional Design
• Just need the design for the Home page and Internal pages - I will do the Coding for the pages in html and/or wordpress.
• Don't worry about the content - just need a design.

```html
<!DOCTYPE html>
<html lang="en">
<head>
<meta charset="utf-8">
<title>VelliFilez – Home</title>
<link rel="stylesheet" href="https://fonts.googleapis.com/css2?family=Roboto:wght@400;500;700&display=swap">
<style>
  :root {
    --page-bg: #efefef;
    --white: #ffffff;
    --brand-blue: #1e8ff2;
    --brand-blue-dark: #1a7fe0;
    --navy: #1b3e72;
    --service-blue: #3d6cc6;
    --body-text: #5a5a5a;
    --divider: #e3e3e3;
    --footer-bg: #2e2e2e;
    --footer-text: #e9e9e9;
    --fab-red: #e32b2b;
    --icon-red: #f0524f;
    --icon-green: #35b83a;
    --icon-blue: #2f6fd1;
    --icon-teal: #2bb3b8;
    --illus-green: #6fd8a8;
  }
  * { box-sizing: border-box; margin: 0; padding: 0; }
  html, body { width: 686px; height: 1200px; overflow: hidden; }
  body { font-family: "Roboto", Arial, sans-serif; background: var(--page-bg); color: var(--body-text); }
  .page { position: relative; width: 686px; height: 1200px; overflow: hidden; }

  .site-header { position: absolute; top: 0; left: 0; width: 686px; height: 53px; background: var(--white); }
  .menu-toggle { position: absolute; left: 50px; top: 19px; width: 19px; height: 14px; }
  .menu-toggle span { position: absolute; left: 0; width: 19px; height: 2px; background: var(--navy); }
  .brand { position: absolute; left: 0; width: 686px; top: 15px; text-align: center; font-size: 20px; font-weight: 700; color: var(--navy); letter-spacing: .5px; }

  .hero { position: absolute; top: 53px; left: 0; width: 686px; height: 250px; background: var(--brand-blue); }
  .hero-title { position: absolute; top: 36px; left: 0; width: 686px; text-align: center; color: var(--white); font-size: 17.5px; font-weight: 700; line-height: 24px; letter-spacing: .4px; text-transform: uppercase; }
  .hero-illustration { position: absolute; top: 82px; left: 10px; width: 666px; height: 166px; background: linear-gradient(90deg, #3ba0f6, #6ab8f8 30%, #e8f1fa 50%, #6ab8f8 70%, #3ba0f6); opacity: .55; border-radius: 4px; }

  .card { position: absolute; left: 50px; width: 587px; background: var(--white); box-shadow: 0 1px 3px rgba(0,0,0,.28); }
  .welcome { top: 249px; height: 132px; text-align: center; padding: 0 40px; }
  .section-title { color: var(--navy); font-size: 18px; font-weight: 700; letter-spacing: 1px; }
  .welcome .section-title { margin-top: 24px; }
  .copy { font-size: 7.4px; line-height: 12px; letter-spacing: .3px; color: var(--body-text); }
  .welcome .copy { margin-top: 9px; }

  .about { top: 406px; height: 171px; }
  .about .section-title { position: absolute; left: 14px; top: 14px; }
  .about-text { position: absolute; left: 14px; top: 44px; width: 352px; }
  .about-text .copy + .copy { margin-top: 12px; }
  .about-illustration { position: absolute; left: 402px; top: 16px; width: 169px; height: 136px; background: radial-gradient(circle at 50% 55%, #8de3bb, var(--illus-green) 70%); box-shadow: 0 1px 3px rgba(0,0,0,.25); }

  .services-band { position: absolute; top: 606px; left: 0; width: 686px; height: 108px; background: var(--brand-blue); }
  .services-band .section-title { color: var(--white); text-align: center; margin-top: 20px; font-weight: 500; letter-spacing: .5px; }

  .services { top: 664px; height: 425px; }
  .service { position: relative; height: 106px; border-bottom: 1px solid var(--divider); }
  .service:last-child { border-bottom: none; height: 107px; }
  .service-icon { position: absolute; left: 44px; top: 38px; width: 30px; height: 30px; }
  .service-divider { position: absolute; left: 119px; top: 10px; width: 1px; height: 86px; background: var(--divider); }
  .service-title { position: absolute; left: 133px; top: 19px; color: var(--service-blue); font-size: 10px; font-weight: 700; letter-spacing: .6px; }
  .service .copy { position: absolute; left: 133px; top: 40px; width: 420px; }
  .read-more { position: absolute; right: 50px; top: 77px; color: var(--brand-blue-dark); font-size: 7.8px; font-weight: 500; text-decoration: underline; }

  .load-more { position: absolute; left: 299px; top: 1118px; width: 88px; height: 21px; border-radius: 3px; background: var(--brand-blue); color: var(--white); font-size: 10px; font-weight: 500; text-align: center; line-height: 21px; }
  .fab { position: absolute; left: 641px; top: 1110px; width: 42px; height: 42px; border-radius: 50%; background: var(--fab-red); box-shadow: 0 2px 4px rgba(0,0,0,.35); }
  .fab::before, .fab::after { content: ""; position: absolute; left: 14px; top: 20px; width: 14px; height: 2px; background: var(--white); }
  .fab::after { transform: rotate(90deg); }

  .site-footer { position: absolute; top: 1168px; left: 0; width: 686px; height: 32px; background: var(--footer-bg); color: var(--footer-text); font-size: 6.5px; text-align: center; line-height: 32px; }
</style>
</head>
<body>
<div class="page">
  <header class="site-header">
    <div class="menu-toggle" aria-label="Menu"><span style="top:0"></span><span style="top:6px"></span><span style="top:12px"></span></div>
    <div class="brand">VelliFilez</div>
  </header>

  <section class="hero">
    <h1 class="hero-title">Lorem Ipsum is simply dummy text of the<br>printing and typesetting</h1>
    <div class="hero-illustration" role="img" aria-label="Row of medical icons: flasks, laptops with heart monitors, first aid kits, pills and clipboards"></div>
  </section>

  <section class="card welcome">
    <h2 class="section-title">WELCOME</h2>
    <p class="copy">Lorem Ipsum is simply dummy text of the printing and typesetting industry. Lorem Ipsum has been the industry's standard dummy text ever since the 1500s, when an unknown printer took a galley of type and scrambled it to make. Lorem Ipsum is simply dummy text of the printing and typesetting industry. Lorem Ipsum has been the industry's standard dummy text ever since the 1500s, whe. Lorem Ipsum is simply dummy text of the printing and typesetting industry. Lorem Ipsum has been the industry's standard .</p>
  </section>

  <section class="card about">
    <h2 class="section-title">ABOUT US</h2>
    <div class="about-text">
      <p class="copy">Lorem Ipsum is simply dummy text of the printing and typesetting industry. Lorem Ipsum has been the industry's standard dummy text ever since the 1500s, when an unknown printer took a galley of type and scrambled it to make. Lorem Ipsum is simply dummy text of the printing and typesetting industry. Lorem Ipsum has been the industry's standard dummy text ever since the 1500s, when an unknown printer took a galley of type and scrambled it to make.</p>
      <p class="copy">Lorem Ipsum is simply dummy text of the printing and typesetting industry. Lorem Ipsum has been the industry's standard dummy text ever since the 1500s, when an unknown printer took a galley of type and scrambled it to make. 1500.</p>
    </div>
    <div class="about-illustration" role="img" aria-label="Illustration of a doctor surrounded by medical equipment on a mint green background"></div>
  </section>

  <section class="services-band">
    <h2 class="section-title">OUR SERVICES</h2>
  </section>

  <section class="card services">
    <article class="service">
      <svg class="service-icon" viewBox="0 0 30 30" fill="none" stroke="var(--icon-red)" stroke-width="2" stroke-linejoin="round"><path d="M8 3h10l6 6v18H8z"/><path d="M18 3v6h6"/></svg>
      <div class="service-divider"></div>
      <h3 class="service-title">LOREM IPSUM IS SIMPLY DUMMY</h3>
      <p class="copy">Lorem Ipsum is simply dummy text of the printing and typesetting industry. Lorem Ipsum has been the industry's standard dummy text ever since the 1500s, when an unknown printer took a galley of type and scrambled it to make.</p>
      <span class="read-more">Read More</span>
    </article>
    <article class="service">
      <svg class="service-icon" viewBox="0 0 30 30" fill="none" stroke="var(--icon-green)" stroke-width="2.4" stroke-linecap="round"><path d="M6 4v8a6 6 0 0 0 12 0V4"/><path d="M12 18v4a5 5 0 0 0 10 0v-5"/><circle cx="22" cy="14" r="3"/></svg>
      <div class="service-divider"></div>
      <h3 class="service-title">LOREM IPSUM IS SIMPLY DUMMY</h3>
      <p class="copy">Lorem Ipsum is simply dummy text of the printing and typesetting industry. Lorem Ipsum has been the industry's standard dummy text ever since the 1500s, when an unknown printer took a galley of type and scrambled it to make.</p>
      <span class="read-more">Read More</span>
    </article>
    <article class="service">
      <svg class="service-icon" viewBox="0 0 30 30" fill="var(--icon-blue)"><circle cx="15" cy="9" r="5.5"/><path d="M4 27v-4a6 6 0 0 1 6-6h10a6 6 0 0 1 6 6v4z"/></svg>
      <div class="service-divider"></div>
      <h3 class="service-title">LOREM IPSUM IS SIMPLY DUMMY</h3>
      <p class="copy">Lorem Ipsum is simply dummy text of the printing and typesetting industry. Lorem Ipsum has been the industry's standard dummy text ever since the 1500s, when an unknown printer took a galley of type and scrambled it to make.</p>
      <span class="read-more">Read More</span>
    </article>
    <article class="service">
      <svg class="service-icon" viewBox="0 0 30 30"><path d="M9 4h17l-4 20H5z" fill="var(--icon-teal)"/><path d="M5 24l1 3h16" fill="none" stroke="var(--icon-teal)" stroke-width="2"/><path d="M11 10h10M10 14h10" stroke="var(--white)" stroke-width="1.6"/></svg>
      <div class="service-divider"></div>
      <h3 class="service-title">LOREM IPSUM IS SIMPLY DUMMY</h3>
      <p class="copy">Lorem Ipsum is simply dummy text of the printing and typesetting industry. Lorem Ipsum has been the industry's standard dummy text ever since the 1500s, when an unknown printer took a galley of type and scrambled it to make.</p>
      <span class="read-more">Read More</span>
    </article>
  </section>

  <div class="load-more">Load More</div>
  <div class="fab" aria-label="Add"></div>

  <footer class="site-footer">Copyright © vellifilez | All Rights Reaserved</footer>
</div>
</body>
</html>
```